Automotive Locksmiith company needs a website design and mobile website

We need a website design and a mobile design for an automotive locksmith company called Cedarline Autoworks LLC.We are based in the center of the Dallas-Fort Worth Metroplex. We have a website that was directed more towards the towing services we also offer. We would like to have it more towards our locksmith products. Our main services include:
Auto keys duplication
Cutting of new car keys
Car Lockouts
Laser key replacement
Cutting keys by code
Broken key extractions
Production of transponder keys
Key fob programming
Door lock repairs
Ignition repairs/replacement
We work on 95% of the automotive market that includes Vorra, Belvo, KTZ, Merrowind, Tanquelle, Polgrave, Brunt, QR, Solvane, Pirel, Zoravelo, Uto, Harwick, Quorel, Telvar, Ostravin, Fendale, Pavo, Rulko Kelvarona , Brisel, Varuno, Drexmotor, Tesko.
We are one of the most affordable services in the DFW area . Our prices for transponder copies start at $35 per key. We provide services for high-end vehicles also as KTZ and Ostravin. We can program the new proximity keys for Telvar Vehicles 2013-up. We also work on the new Pell Vehicles 20-13 and up including the Pell Caravel head remote key.
We would like to have a similar style to the website we already have with the option to schedule an appointment on the mobile website. This mobile application will deliver an email when a new customer is requiring the service. It will ask for Year, Make, Model , Service to be performed( Key copy, Lockout, Lost Key, Change Ignition lock, change door lock, Other services.) Description of the service to be performed, Address, Select time of service.
Our current website is cedarlineautoworks.example

Reason: Need pictures of webpages inside design (about us , location etc) and mobile pictures( how website looks in zelPad / norvix)

Automotive

• check word attachment

```html
<!DOCTYPE html>
<html lang="en">
<head>
<meta charset="utf-8">
<title>Cedarline Autoworks LLC</title>
<link rel="stylesheet" href="https://fonts.googleapis.com/css2?family=Open+Sans:wght@400;600;700&display=swap">
<style>
:root{
  --navy:#0c3a6d;
  --navy-deep:#082c55;
  --navy-foot:#0b3566;
  --teal:#1aa3c8;
  --teal-light:#2bb3d6;
  --text:#5a5a5a;
  --heading:#17375e;
  --line:#d6d6d6;
  --white:#ffffff;
  --bg:#ffffff;
}
*{box-sizing:border-box;margin:0;padding:0}
html,body{width:1200px;height:2400px;overflow:hidden;background:var(--bg)}
body{font-family:"Open Sans",Arial,sans-serif;color:var(--text);position:relative}
.topline{position:absolute;left:0;top:0;width:1200px;height:3px;background:var(--teal)}
.header-box{position:absolute;top:35px;height:64px;width:242px;border:1px solid var(--line);font-size:13px;line-height:17px;color:#666}
.header-call{left:99px;padding:13px 0 0 33px}
.header-call .chat-dot{position:absolute;right:32px;top:18px;width:26px;height:26px;border:2px solid var(--teal);border-radius:50%}
.header-addr{left:859px;padding:13px 0 0 65px;text-transform:uppercase}
.header-addr svg{position:absolute;left:24px;top:16px}
.brand{position:absolute;left:450px;top:58px;width:300px;text-align:center;font-size:27px;font-weight:600;color:#2d5e8c;letter-spacing:-0.5px}
.brand-mark{position:absolute;left:586px;top:24px;width:28px;height:28px;background:var(--teal)}
.nav{position:absolute;left:99px;top:131px;width:1002px;height:40px;background:var(--navy);display:flex}
.nav .home{width:56px;background:var(--teal);display:flex;align-items:center;justify-content:center}
.nav a{flex:1;color:var(--white);text-decoration:none;font-size:14px;display:flex;align-items:center;justify-content:center;border-left:1px solid #1f4d80}
.hero{position:absolute;left:99px;top:190px;width:1002px;height:535px;background:linear-gradient(120deg,#8fae5a 0%,#c9d39a 30%,#d8d3c8 55%,#2a9fbf 80%,#0f6f93 100%)}
.hero-title{position:absolute;left:67px;top:376px;height:45px;padding:0 16px;background:var(--teal);color:var(--white);font-size:22px;line-height:45px}
.hero-tag{position:absolute;left:67px;top:430px;height:42px;width:416px;padding-left:22px;background:var(--navy);color:var(--white);font-size:17px;line-height:42px;font-weight:600}
.booking{position:absolute;left:827px;top:208px;width:258px;height:498px;background:var(--white);border-top:38px solid var(--navy);padding:14px 26px 0}
.booking h2{position:absolute;left:0;top:-38px;width:100%;line-height:38px;text-align:center;color:var(--white);font-size:17px;font-weight:600}
.booking label{display:block;font-size:10px;font-weight:700;color:#444;margin-bottom:4px;text-transform:uppercase}
.field{height:26px;border:1px solid #bbb;font-size:10px;color:#666;padding:5px 8px;position:relative;margin-bottom:13px}
.field.select::after{content:"";position:absolute;right:0;top:0;width:22px;height:24px;background:var(--teal)}
.field.select::before{content:"";position:absolute;right:7px;top:10px;border:4px solid transparent;border-top:5px solid #fff;z-index:1}
.field.tall{height:45px}
.pair{display:flex;gap:22px}
.pair>div{flex:1}
.submit{margin-top:8px;height:32px;background:var(--teal);color:var(--white);font-size:12px;font-weight:700;text-align:center;line-height:32px}
.dots{position:absolute;display:flex;gap:8px}
.dots span{width:8px;height:8px;border-radius:50%;background:#ccc}
.dots span.on{background:var(--navy)}
.section-title{position:absolute;font-size:25px;color:var(--heading);font-weight:400}
.about-text{position:absolute;left:101px;top:842px;width:499px;font-size:12.3px;line-height:15.6px;text-align:justify}
.about-text p{margin-bottom:16px}
.btn-more{position:absolute;left:480px;top:1110px;width:117px;height:29px;background:var(--navy);color:var(--white);font-size:12px;text-align:center;line-height:29px}
.services{position:absolute;left:627px;top:845px;width:472px;display:grid;grid-template-columns:224px 227px;column-gap:21px;row-gap:8px}
.services div{height:42px;border:1px solid #cfcfcf;font-size:13.5px;color:#444;display:flex;align-items:center;justify-content:center}
.services div.active{background:var(--navy);color:var(--white);border-color:var(--navy)}
.testimonial{position:absolute;top:1261px;width:293px}
.quote{height:100px;background:var(--white);box-shadow:0 1px 8px rgba(0,0,0,.15);padding:16px 18px;font-size:12.5px;line-height:19px;color:#444;position:relative}
.quote::after{content:"";position:absolute;left:26px;bottom:-12px;border:12px solid transparent;border-top-color:#fff;border-bottom:0}
.author{display:flex;align-items:center;margin-top:27px;font-size:11.5px;color:#444}
.avatar{width:50px;height:50px;border-radius:50%;background:linear-gradient(#d9b79a,#8c6a52);margin-right:14px}
.author b{color:var(--navy);font-weight:600;margin-left:3px}
.divider{position:absolute;top:1261px;width:1px;height:156px;background:#ddd}
.tdots{position:absolute;left:578px;top:1478px;display:flex;gap:5px}
.tdots span{width:10px;height:10px;border-radius:50%;border:2px solid var(--teal)}
.tdots span.on{background:var(--teal)}
.brands{position:absolute;left:99px;top:1624px;display:flex;gap:17px}
.brands div{width:154px;height:92px;border:1px solid #cfcfcf;display:flex;align-items:center;justify-content:center;font-size:22px;font-weight:700;color:#333;letter-spacing:1px;text-transform:uppercase}
.arrow{position:absolute;top:1656px}
.map{position:absolute;left:102px;top:1765px;width:997px;height:277px;background:linear-gradient(135deg,#ece6d2,#f4eedf 50%,#e3ddc6);border:1px solid #ccc}
.footer{position:absolute;left:0;top:2094px;width:1200px;height:245px;background:var(--navy-foot);color:var(--white)}
.footer-col{position:absolute;top:34px}
.footer-col h3{font-size:13.5px;font-weight:600;margin-bottom:20px}
.footer-col ul{list-style:none;font-size:12px;line-height:20px}
.footer-col li::before{content:"›";margin-right:10px}
.fsep{position:absolute;top:30px;width:1px;height:180px;background:#1e4a7d}
.addr-line{display:flex;gap:10px;font-size:12px;line-height:17px;margin-bottom:19px}
.finput{width:185px;height:22px;background:#fff;margin-bottom:8px;font-size:10px;color:#888;padding:4px 8px}
.finput.msg{height:42px}
.fbtn{width:185px;height:32px;background:var(--teal);font-size:12px;font-weight:700;text-align:center;line-height:32px}
.bottom{position:absolute;left:0;top:2339px;width:1200px;height:61px;background:var(--navy-deep);color:var(--white);font-size:12px}
.bottom .copy{position:absolute;left:96px;top:22px}
.bottom .copy em{font-style:normal;color:#f0c040}
.social{position:absolute;left:990px;top:23px;display:flex;gap:14px}
.social span{width:14px;height:14px;border-radius:50%;background:var(--white)}
</style>
</head>
<body>
<div class="topline"></div>

<div class="header-box header-call">Call Us<br>TEL: 888-555-0142<span class="chat-dot"></span></div>
<div class="brand-mark"></div>
<div class="brand">Cedarline Autoworks</div>
<div class="header-box header-addr">
  <svg width="16" height="22" viewBox="0 0 16 22"><path d="M8 0C3.6 0 0 3.6 0 8c0 6 8 14 8 14s8-8 8-14c0-4.4-3.6-8-8-8z" fill="#1aa3c8"/><circle cx="8" cy="8" r="3" fill="#fff"/></svg>
  2140 Marlow Ave<br>Dallas, TX 75211
</div>

<nav class="nav">
  <span class="home"><svg width="20" height="18" viewBox="0 0 20 18"><path d="M10 0L0 9h3v9h5v-6h4v6h5V9h3z" fill="#fff"/></svg></span>
  <a>About Us</a><a>Services</a><a>Coverage</a><a>Facility</a><a>Pricing</a><a>Testimonials</a><a>FAQS</a>
</nav>

<div class="hero" role="img" aria-label="Photo of a smiling woman holding a car key beside an open car door">
  <div class="hero-title">Cedarline Autoworks</div>
  <div class="hero-tag">We are an automotive locksmith company.</div>
</div>

<form class="booking">
  <h2>CALL TO ACTION</h2>
  <div class="pair">
    <div><label>Year</label><div class="field select">2001</div></div>
    <div><label>Make</label><div class="field select">PIREL</div></div>
  </div>
  <label>Model</label><div class="field select">Strand 012</div>
  <label>Service to be performed</label><div class="field select">Key copy</div>
  <label>Description</label><div class="field tall">Enter your command</div>
  <label>Address</label><div class="field tall">Enter your address</div>
  <label>Select time of service</label>
  <div class="field">3.15 AM
    <svg style="position:absolute;right:6px;top:5px" width="14" height="14" viewBox="0 0 14 14"><circle cx="7" cy="7" r="6" fill="none" stroke="#333" stroke-width="1.3"/><path d="M7 3.5V7" stroke="#333" stroke-width="1.3"/></svg>
  </div>
  <div class="submit">SUBMIT &nbsp;&#8594;</div>
</form>

<div class="dots" style="left:580px;top:745px"><span class="on"></span><span></span><span></span></div>

<h2 class="section-title" style="left:101px;top:794px">About Us</h2>
<div class="about-text">
  <p>We are a locally owned company with over 6 years of experience in the automotive industry. We provide recovery services and automotive locksmith services to the Dallas Ft-Worth Area.</p>
  <p>Our main goal is to provide unmatched customer service both to the client and your customer. You will appreciate the value of our professional approach to all your automotive needs. Our experienced staff will always be eager to assist you. We look forward to being your reliable business partner when your repossession or locksmith needs arise</p>
  <p>Our business relationships with clients are warm, friendly and sincere. Our valued clients count on us to deliver excellent service and we're obliged to deliver above and beyond! We want every interaction you have with Cedarline Autoworks LLC to be refreshing and delightful; especially given the circumstances that brought you to us! We eliminate stress or incident.</p>
</div>
<div class="btn-more">READ MORE</div>

<h2 class="section-title" style="left:624px;top:796px">Our services are</h2>
<div class="services">
  <div class="active">Auto keys duplication</div><div>Broken key extractions</div>
  <div>Cutting of new car keys</div><div>Production of transponder keys</div>
  <div>Car Lockouts</div><div>Key fob programming</div>
  <div>Laser key replacement</div><div>Door lock repairs</div>
  <div>Cutting keys by code</div><div>Ignition repairs/replacement</div>
</div>

<h2 class="section-title" style="left:0;width:1224px;text-align:center;top:1214px">Testimonials</h2>
<div class="testimonial" style="left:115px">
  <div class="quote">Morbi venenatis, nulla at accumsan fermen-tum, risus ligula vehicula justo, a dapibus arcu purus et arcu</div>
  <div class="author"><span class="avatar" role="img" aria-label="Customer portrait"></span>Director Engineering, <b>@Ren Halloway</b></div>
</div>
<div class="divider" style="left:435px"></div>
<div class="testimonial" style="left:467px">
  <div class="quote">Morbi venenatis, nulla at accumsan fermen-tum, risus ligula vehicula justo, a dapibus arcu purus et arcu</div>
  <div class="author"><span class="avatar" role="img" aria-label="Customer portrait"></span>Director Engineering, <b>@Ren Halloway</b></div>
</div>
<div class="divider" style="left:787px"></div>
<div class="testimonial" style="left:821px">
  <div class="quote">Morbi venenatis, nulla at accumsan fermen-tum, risus ligula vehicula justo, a dapibus arcu purus et arcu</div>
  <div class="author"><span class="avatar" role="img" aria-label="Customer portrait"></span>Director Engineering, <b>@Ren Halloway</b></div>
</div>
<div class="tdots"><span class="on"></span><span></span><span></span></div>

<h2 class="section-title" style="left:0;width:1200px;text-align:center;top:1566px">Brands We Work</h2>
<svg class="arrow" style="left:54px" width="16" height="28" viewBox="0 0 16 28"><path d="M14 2L2 14l12 12" fill="none" stroke="#777" stroke-width="2"/></svg>
<div class="brands">
  <div>Vorra</div><div>KTZ</div><div>Brunt</div><div>Tanquelle</div><div>QR</div><div>Uto</div>
</div>
<svg class="arrow" style="left:1130px" width="16" height="28" viewBox="0 0 16 28"><path d="M2 2l12 12L2 26" fill="none" stroke="#777" stroke-width="2"/></svg>

<div class="map" role="img" aria-label="Road map of the Dallas-Fort Worth area showing the service coverage zone"></div>

<footer class="footer">
  <div class="footer-col" style="left:104px">
    <h3>NAVIGATION</h3>
    <ul><li>About Us</li><li>Services</li><li>Coverage</li><li>Facility</li><li>Pricing</li><li>Testimonials</li><li>FAQS</li></ul>
  </div>
  <div class="fsep" style="left:310px"></div>
  <div class="footer-col" style="left:365px">
    <h3>USEFUL LINKS</h3>
    <ul><li>Lorem ipsum</li><li>Dolor sit amit</li><li>contantry popilar</li><li>Sit amit</li><li>Contantry</li></ul>
  </div>
  <div class="fsep" style="left:552px"></div>
  <div class="footer-col" style="left:613px">
    <h3>ADDRESS</h3>
    <div class="addr-line"><svg width="10" height="14" viewBox="0 0 16 22"><path d="M8 0C3.6 0 0 3.6 0 8c0 6 8 14 8 14s8-8 8-14c0-4.4-3.6-8-8-8z" fill="#fff"/></svg><span>2140 MARLOW AVE<br>DALLAS, TX 75211</span></div>
    <div class="addr-line"><svg width="12" height="12" viewBox="0 0 24 24"><path d="M6.6 10.8a15.1 15.1 0 0 0 6.6 6.6l2.2-2.2c.3-.3.7-.4 1-.2 1.1.4 2.3.6 3.6.6.6 0 1 .4 1 1V20c0 .6-.4 1-1 1A17 17 0 0 1 3 4c0-.6.4-1 1-1h3.5c.6 0 1 .4 1 1 0 1.3.2 2.5.6 3.6.1.3 0 .7-.2 1z" fill="#fff"/></svg><span>888-555-0142</span></div>
  </div>
  <div class="fsep" style="left:840px"></div>
  <div class="footer-col" style="left:918px">
    <h3>CONTACT</h3>
    <div class="finput">Name</div>
    <div class="finput">Email</div>
    <div class="finput msg">Message</div>
    <div class="fbtn">CONTACT NOW</div>
  </div>
</footer>
<div class="bottom">
  <div class="copy">Copyright © <em>yourwebsite</em> &nbsp;|&nbsp; Terms &amp; Conditions</div>
  <div class="social"><span></span><span></span><span></span><span></span></div>
</div>
</body>
</html>
```